KAVLO ZenOS app needs a fun consumer interface design

KAVLO is a file transfer app aimed at consumers to help them get files onto their ZenOS devices. The app is based around each user having a personalised upload web address, and the ability to issue temporary time limited upload codes to friends and colleagues that they can use to send them files. The first version is already live in the widget shelf but we are working on a second, simplified version. You can see the screen shots for this on www.kavlo-example.com and I have attached a quick guide to app flow. The app now looks like a standard templated ZenOS 7 app. We need a design for the app that give it its own look, whilst retaining the standard ZenOS cues. It needs to look good on Palmo and Slabbo. We have a far east techno feel to the app at the moment with our characters, and we want to keep the logo. The website is currently a simple template, there's an ongoing competition to redesign that too - http://jobs.pitchmarket-example.com/job.aspx?id=813964
We have a working app with a reasonable design - we are looking for someone to take that design, add the polish a professional designer can bring, to make it pixel perfect and stand out as an app that has great design as well as great functionality.
We are also looking for something that works well on Palmo and Slabbo. See the attached screenshots of the Slabbo version - we want that version to look beautiful, not the big empty screen it is now.
Updates
Thanks for the designs so far, they look good. Could you draw them up for Slabbo size screens too please. The signup/login page and new code pages I think need the most attention as each page doesn't collect that much information, and so a lot of the screen is currently blank. I think we need some sort of background to set the content into for these pages.
(file 4 and file 6 are Slabbo screenshots)
The old app is installable for free from the Widget Shelf if that helps you get a feel for it on the Slabbo.
Target Market(s)
Consumers, techno savvy
Industry/Entity Type
Store
Font styles to use
Look and feel
Each slider illustrates characteristics of the customer's brand and the style your logo design should communicate.

```html
<!DOCTYPE html>
<html lang="en">
<head>
<meta charset="utf-8">
<title>KAVLO – Slabbo transfers screen</title>
<link rel="stylesheet" href="https://fonts.googleapis.com/css2?family=Open+Sans:wght@300;400;600&display=swap">
<style>
  :root {
    --backdrop-top: #f1f1f1;
    --backdrop-bottom: #d6d6d6;
    --sky: #2bb3f6;
    --sky-soft: #86d3fb;
    --tab-strip: #8fd4fb;
    --tab-strip-soft: #c3e9fd;
    --row-bg: #ffffff;
    --row-gap: #e9ecee;
    --ink: #3b3b3b;
    --ink-soft: #6a6a6a;
    --ink-faint: #a9a9a9;
    --status-bar: #2b2b2b;
    --dock: #cbcbcb;
    --dock-icon: #ffffff;
    --avatar-tone: #c9a98e;
  }
  * { box-sizing: border-box; margin: 0; padding: 0; }
  html, body {
    width: 1126px; height: 1200px; overflow: hidden;
    background: linear-gradient(var(--backdrop-top), var(--backdrop-bottom));
    font-family: "Open Sans", Arial, sans-serif;
  }
  .screen {
    position: absolute; left: 131px; top: 24px;
    width: 864px; height: 1152px;
    background: var(--row-gap); overflow: hidden;
    box-shadow: 0 10px 40px rgba(0,0,0,.12);
  }
  .status-bar {
    height: 22px; background: var(--status-bar); color: #fff;
    font-size: 13px; display: flex; align-items: center;
    justify-content: space-between; padding: 0 12px; position: relative; z-index: 2;
  }
  .status-bar .clock { position: absolute; left: 50%; transform: translateX(-50%); }
  .signal { display: inline-flex; align-items: flex-end; gap: 1px; margin-right: 4px; }
  .signal i { display: block; width: 2px; background: #fff; }
  .battery { display: inline-block; width: 22px; height: 10px; border: 1px solid #fff; margin-left: 4px; vertical-align: middle; position: relative; }
  .battery::after { content: ""; position: absolute; inset: 1px 9px 1px 1px; background: #fff; }
  .profile-header {
    position: relative; height: 272px; background: var(--sky);
    overflow: hidden;
  }
  .profile-header .sheen {
    position: absolute; inset: 0;
    background: var(--sky-soft);
    clip-path: polygon(416px 0, 100% 0, 100% 100%, 536px 100%);
    opacity: .85;
  }
  .avatar {
    position: absolute; left: 50%; top: 36px; transform: translateX(-50%);
    width: 124px; height: 124px; border-radius: 50%;
    border: 5px solid #fff;
    background: radial-gradient(circle at 50% 45%, #e2c2a6, var(--avatar-tone) 60%, #8a7563);
  }
  .profile-name {
    position: absolute; top: 176px; width: 100%; text-align: center;
    color: #fff; font-size: 22px; font-weight: 400;
  }
  .tab-strip {
    position: absolute; left: 0; right: 0; bottom: 0; height: 42px;
    background: var(--tab-strip); display: flex;
  }
  .tab-strip .sheen-strip {
    position: absolute; inset: 0; background: var(--tab-strip-soft);
    clip-path: polygon(520px 0, 100% 0, 100% 100%, 536px 100%);
  }
  .tab-strip .tab { flex: 1; display: flex; align-items: center; justify-content: center; position: relative; }
  .transfer-list { list-style: none; }
  .transfer-row {
    height: 68px; margin-bottom: 4px; background: var(--row-bg);
    display: flex; align-items: center; padding: 0 48px 0 30px;
  }
  .transfer-row .spinner { width: 24px; height: 24px; margin-right: 26px; }
  .transfer-row .code { font-size: 21px; color: var(--ink); flex: 1; }
  .transfer-row .meta { text-align: right; }
  .transfer-row .when { font-size: 14px; color: var(--ink-soft); }
  .transfer-row .size { font-size: 10px; color: var(--ink-faint); margin-top: 3px; }
  .dock {
    position: absolute; left: 0; right: 0; bottom: 0; height: 58px;
    background: var(--dock); display: flex;
  }
  .dock .dock-item { flex: 1; display: flex; align-items: center; justify-content: center; }
</style>
</head>
<body>
<main class="screen">
  <div class="status-bar">
    <span><span class="signal"><i style="height:3px"></i><i style="height:5px"></i><i style="height:7px"></i><i style="height:9px"></i></span>NEXO</span>
    <span class="clock">10:35 AM</span>
    <span>65%<span class="battery"></span></span>
  </div>

  <header class="profile-header">
    <div class="sheen"></div>
    <div class="avatar" role="img" aria-label="User profile photo"></div>
    <div class="profile-name">Lenora</div>
    <nav class="tab-strip">
      <div class="sheen-strip"></div>
      <div class="tab">
        <svg width="24" height="24" viewBox="0 0 24 24" fill="none" stroke="#fff" stroke-width="2.4" stroke-linecap="round"><path d="M10 14l4-4"/><path d="M8.5 11.5l-2 2a3 3 0 004.2 4.2l2-2"/><path d="M15.5 12.5l2-2a3 3 0 00-4.2-4.2l-2 2"/></svg>
      </div>
      <div class="tab">
        <svg width="28" height="22" viewBox="0 0 28 22" fill="none" stroke="#fff" stroke-width="2"><rect x="3" y="3" width="22" height="16"/><path d="M3 3l11 9 11-9"/></svg>
      </div>
      <div class="tab">
        <svg width="30" height="22" viewBox="0 0 30 22" fill="none" stroke="#fff" stroke-width="1.8"><path d="M8 18h15a5 5 0 000-10 7 7 0 00-13-1 5.5 5.5 0 00-2 11z"/></svg>
      </div>
    </nav>
  </header>

  <ul class="transfer-list">
    <li class="transfer-row"><svg class="spinner" viewBox="0 0 24 24" fill="none" stroke="#2bb3f6" stroke-width="2"><path d="M12 3a9 9 0 11-8.5 6"/><circle cx="12" cy="12" r="3" fill="#2bb3f6" stroke="none"/></svg><span class="code">RX105JJB</span><div class="meta"><div class="when">Today at 15:40</div><div class="size">184.45 kb (910.100.2002)</div></div></li>
    <li class="transfer-row"><svg class="spinner" viewBox="0 0 24 24" fill="none" stroke="#2bb3f6" stroke-width="2"><path d="M12 3a9 9 0 11-8.5 6"/><circle cx="12" cy="12" r="3" fill="#2bb3f6" stroke="none"/></svg><span class="code">RX105JJB</span><div class="meta"><div class="when">Today at 15:40</div><div class="size">184.45 kb (910.100.2002)</div></div></li>
    <li class="transfer-row"><svg class="spinner" viewBox="0 0 24 24" fill="none" stroke="#2bb3f6" stroke-width="2"><path d="M12 3a9 9 0 11-8.5 6"/><circle cx="12" cy="12" r="3" fill="#2bb3f6" stroke="none"/></svg><span class="code">RX105JJB</span><div class="meta"><div class="when">Today at 15:40</div><div class="size">184.45 kb (910.100.2002)</div></div></li>
    <li class="transfer-row"><svg class="spinner" viewBox="0 0 24 24" fill="none" stroke="#2bb3f6" stroke-width="2"><path d="M12 3a9 9 0 11-8.5 6"/><circle cx="12" cy="12" r="3" fill="#2bb3f6" stroke="none"/></svg><span class="code">RX105JJB</span><div class="meta"><div class="when">Today at 15:40</div><div class="size">184.45 kb (910.100.2002)</div></div></li>
    <li class="transfer-row"><svg class="spinner" viewBox="0 0 24 24" fill="none" stroke="#2bb3f6" stroke-width="2"><path d="M12 3a9 9 0 11-8.5 6"/><circle cx="12" cy="12" r="3" fill="#2bb3f6" stroke="none"/></svg><span class="code">RX105JJB</span><div class="meta"><div class="when">Today at 15:40</div><div class="size">184.45 kb (910.100.2002)</div></div></li>
    <li class="transfer-row"><svg class="spinner" viewBox="0 0 24 24" fill="none" stroke="#2bb3f6" stroke-width="2"><path d="M12 3a9 9 0 11-8.5 6"/><circle cx="12" cy="12" r="3" fill="#2bb3f6" stroke="none"/></svg><span class="code">RX105JJB</span><div class="meta"><div class="when">Today at 15:40</div><div class="size">184.45 kb (910.100.2002)</div></div></li>
    <li class="transfer-row"><svg class="spinner" viewBox="0 0 24 24" fill="none" stroke="#2bb3f6" stroke-width="2"><path d="M12 3a9 9 0 11-8.5 6"/><circle cx="12" cy="12" r="3" fill="#2bb3f6" stroke="none"/></svg><span class="code">RX105JJB</span><div class="meta"><div class="when">Today at 15:40</div><div class="size">184.45 kb (910.100.2002)</div></div></li>
    <li class="transfer-row"><svg class="spinner" viewBox="0 0 24 24" fill="none" stroke="#2bb3f6" stroke-width="2"><path d="M12 3a9 9 0 11-8.5 6"/><circle cx="12" cy="12" r="3" fill="#2bb3f6" stroke="none"/></svg><span class="code">RX105JJB</span><div class="meta"><div class="when">Today at 15:40</div><div class="size">184.45 kb (910.100.2002)</div></div></li>
    <li class="transfer-row"><svg class="spinner" viewBox="0 0 24 24" fill="none" stroke="#2bb3f6" stroke-width="2"><path d="M12 3a9 9 0 11-8.5 6"/><circle cx="12" cy="12" r="3" fill="#2bb3f6" stroke="none"/></svg><span class="code">RX105JJB</span><div class="meta"><div class="when">Today at 15:40</div><div class="size">184.45 kb (910.100.2002)</div></div></li>
    <li class="transfer-row"><svg class="spinner" viewBox="0 0 24 24" fill="none" stroke="#2bb3f6" stroke-width="2"><path d="M12 3a9 9 0 11-8.5 6"/><circle cx="12" cy="12" r="3" fill="#2bb3f6" stroke="none"/></svg><span class="code">RX105JJB</span><div class="meta"><div class="when">Today at 15:40</div><div class="size">184.45 kb (910.100.2002)</div></div></li>
    <li class="transfer-row"><svg class="spinner" viewBox="0 0 24 24" fill="none" stroke="#2bb3f6" stroke-width="2"><path d="M12 3a9 9 0 11-8.5 6"/><circle cx="12" cy="12" r="3" fill="#2bb3f6" stroke="none"/></svg><span class="code">RX105JJB</span><div class="meta"><div class="when">Today at 15:40</div><div class="size">184.45 kb (910.100.2002)</div></div></li>
  </ul>

  <nav class="dock">
    <div class="dock-item"><svg width="28" height="28" viewBox="0 0 28 28" fill="var(--dock-icon)"><circle cx="14" cy="9" r="5"/><path d="M4 25c0-6 4.5-9 10-9s10 3 10 9z"/></svg></div>
    <div class="dock-item"><svg width="26" height="28" viewBox="0 0 26 28" fill="var(--dock-icon)"><path d="M13 3a2 2 0 012 2v1a7 7 0 015 7v6l3 3H3l3-3v-6a7 7 0 015-7V5a2 2 0 012-2z"/><circle cx="13" cy="25" r="2.5"/></svg></div>
    <div class="dock-item"><svg width="30" height="30" viewBox="0 0 24 24" fill="none" stroke="var(--dock-icon)" stroke-width="2.6" stroke-linecap="round"><path d="M10 14l4-4"/><path d="M8.5 11.5l-2 2a3 3 0 004.2 4.2l2-2"/><path d="M15.5 12.5l2-2a3 3 0 00-4.2-4.2l-2 2"/></svg></div>
    <div class="dock-item"><svg width="30" height="30" viewBox="0 0 30 30"><g fill="var(--dock-icon)"><circle cx="15" cy="15" r="9"/><rect x="12.5" y="2" width="5" height="26" rx="1"/><rect x="12.5" y="2" width="5" height="26" rx="1" transform="rotate(60 15 15)"/><rect x="12.5" y="2" width="5" height="26" rx="1" transform="rotate(120 15 15)"/></g><circle cx="15" cy="15" r="3.5" fill="var(--dock)"/></svg></div>
  </nav>
</main>
</body>
</html>
```